Esthetically Pleasing Core Values and Brand Promise for Accounting Firm

I would like a cohesive design that ties together my core values and brand promise. My firm, Maple Finch Advisory, provides accounting work to small businesses. I prefer modern and clean designs. I want my Core Values and Brand Promise to represent me - sole entrepreneur, married, mother of two kids, modern esthetics, clean lines, organized, colorful (teals, greys, white, yellows)

Industry/Entity Type

Public Accounting

Colors
33b8a4

```html
<!DOCTYPE html>
<html lang="en">
<head>
<meta charset="utf-8">
<title>Maple Finch Advisory – Core Values and Brand Promise</title>
<link rel="stylesheet" href="https://fonts.googleapis.com/css2?family=Montserrat:wght@300;700;800;900&family=Open+Sans:wght@400;600&display=swap">
<style>
  :root {
    --teal: #33b8a4;
    --teal-deep: #1f9a8f;
    --ink: #222428;
    --grey: #8c9096;
    --line: #c9ccd0;
    --paper: #f7f6f8;
    --panel: #ffffff;
    --backdrop: #e6e8ea;
  }
  * { box-sizing: border-box; margin: 0; padding: 0; }
  html, body { width: 1200px; height: 800px; overflow: hidden; }
  body {
    background: var(--backdrop);
    font-family: "Open Sans", Arial, sans-serif;
    color: var(--ink);
    display: flex; align-items: center; justify-content: center;
  }
  .flyer {
    position: relative;
    width: 600px; height: 780px;
    background: var(--paper);
    box-shadow: 0 6px 24px rgba(0,0,0,.15);
    overflow: hidden;
  }
  .hero-photo {
    position: absolute; top: 0; right: 0;
    width: 470px; height: 240px;
    background: linear-gradient(100deg, rgba(247,246,248,1) 0%, rgba(205,208,214,.8) 35%, #a7acb5 70%, #8e939c 100%);
    -webkit-mask-image: linear-gradient(to bottom, #000 70%, transparent 100%);
            mask-image: linear-gradient(to bottom, #000 70%, transparent 100%);
  }
  .brand-name {
    position: absolute; left: 30px; top: 84px;
    font-family: "Montserrat", Arial, sans-serif;
    font-weight: 300; color: var(--teal);
    font-size: 30px; line-height: 1.05; letter-spacing: 2px;
    text-transform: uppercase;
  }
  .panel {
    position: absolute; left: 56px; width: 516px;
    background: var(--panel);
    border: 1px solid var(--line);
  }
  .panel--values { top: 206px; height: 258px; }
  .panel--promise { top: 476px; height: 268px; }
  .band {
    background: var(--teal); color: #fff;
    font-family: "Montserrat", Arial, sans-serif; font-weight: 900;
    font-size: 27px; letter-spacing: .5px; text-transform: uppercase;
    text-align: center; height: 44px; line-height: 44px;
    margin: 10px -10px 0;
  }
  .columns { display: flex; padding: 12px 8px 0; }
  .column {
    flex: 1; text-align: center; padding: 0 6px;
    border-left: 2px dotted var(--line);
  }
  .column:first-child { border-left: none; }
  .icon {
    width: 56px; height: 56px; margin: 0 auto 10px;
    border-radius: 50%; background: var(--teal);
    box-shadow: 0 0 0 4px #fff, 0 2px 6px 4px rgba(0,0,0,.18);
    display: flex; align-items: center; justify-content: center;
  }
  .value-title {
    font-family: "Montserrat", Arial, sans-serif; font-weight: 800;
    color: var(--teal); font-size: 12px; text-transform: uppercase;
    white-space: nowrap; margin-bottom: 4px;
  }
  .value-text { font-size: 10.5px; line-height: 1.35; }
  .promise-line {
    font-family: "Montserrat", Arial, sans-serif; font-weight: 900;
    font-size: 19px; text-transform: uppercase; text-align: center;
    margin-top: 10px; letter-spacing: .2px;
  }
  .panel--promise .columns { padding-top: 10px; }
  .panel--promise .column { padding: 0 16px; }
  .footer-strip {
    position: absolute; left: 0; right: 0; bottom: 0; height: 30px;
    background: var(--teal);
  }
</style>
</head>
<body>
<main class="flyer">
  <div class="hero-photo" role="img" aria-label="Photo of an accountant's hands using a calculator and pen over paperwork"></div>
  <div class="brand-name">Maple<br>Finch<br>Advisory</div>

  <section class="panel panel--values">
    <h2 class="band">Core Values</h2>
    <div class="columns">
      <article class="column">
        <div class="icon"><svg width="28" height="28" viewBox="0 0 28 28" fill="none" stroke="#fff" stroke-width="2" stroke-linecap="round" stroke-linejoin="round"><path d="M14 24V5M7 12l7-7 7 7"/></svg></div>
        <h3 class="value-title">Empower</h3>
        <p class="value-text">we are dedicated, appreciative and respectful of people's time and purpose.</p>
      </article>
      <article class="column">
        <div class="icon"><svg width="28" height="28" viewBox="0 0 28 28" fill="none" stroke="#fff" stroke-width="2" stroke-linecap="round"><circle cx="14" cy="14" r="10"/><circle cx="14" cy="11" r="3.5"/><path d="M8 21c1.5-3 3.5-4.5 6-4.5s4.5 1.5 6 4.5"/></svg></div>
        <h3 class="value-title">Client Focused</h3>
        <p class="value-text">we provide a personal service that goes above the standards of professional care.</p>
      </article>
      <article class="column">
        <div class="icon"><svg width="30" height="28" viewBox="0 0 30 28" fill="none" stroke="#fff" stroke-width="2" stroke-linecap="round" stroke-linejoin="round"><path d="M15 4v19M9 24h12M5 8h20M5 8l-3 8h6zM25 8l-3 8h6z"/></svg></div>
        <h3 class="value-title">Rectitude</h3>
        <p class="value-text">we know the difference between what we have the right to do &amp; what the right thing to do is.</p>
      </article>
      <article class="column">
        <div class="icon"><svg width="28" height="28" viewBox="0 0 28 28" fill="none" stroke="#fff" stroke-width="2" stroke-linecap="round" stroke-linejoin="round"><circle cx="14" cy="14" r="10"/><path d="M9 14l3.5 3.5L19 11"/></svg></div>
        <h3 class="value-title">Relentless</h3>
        <p class="value-text">we believe that the longer we try to do our best, the better we become.</p>
      </article>
    </div>
  </section>

  <section class="panel panel--promise">
    <h2 class="band">Brand Promise</h2>
    <p class="promise-line">Trust, Transparency and Dependability</p>
    <div class="columns">
      <article class="column">
        <div class="icon"><svg width="26" height="28" viewBox="0 0 26 28" fill="none" stroke="#fff" stroke-width="2" stroke-linecap="round" stroke-linejoin="round"><path d="M5 3h12l4 4v18H5z"/><path d="M9 19l8-8"/><circle cx="10" cy="12" r="1.5"/><circle cx="16" cy="18" r="1.5"/></svg></div>
        <h3 class="value-title">Tax</h3>
        <p class="value-text">Maple Finch provides all clients with a trusted tax advisor who provides accuracy in all filings and ensures your compliance with all government agencies.</p>
      </article>
      <article class="column">
        <div class="icon"><svg width="26" height="28" viewBox="0 0 26 28" fill="none" stroke="#fff" stroke-width="2" stroke-linejoin="round"><rect x="5" y="3" width="16" height="22" rx="2"/><rect x="8" y="6" width="10" height="5"/><path d="M9 15h1M13 15h1M17 15h0M9 19h1M13 19h1M17 19h0M9 22h1M13 22h1" stroke-linecap="round"/></svg></div>
        <h3 class="value-title">Accounting</h3>
        <p class="value-text">Maple Finch provides all business owners with the financial visibility needed to foster growth and facilitate goals.</p>
      </article>
    </div>
  </section>

  <div class="footer-strip"></div>
</main>
</body>
</html>
```